Hi, Looking for an upgraded business card to the aged one attached. Open to suggestions and no real limitations, but if your going to use a picture of a taxi i think it should be vector based rather than a full color picture. I've uploaded a 2 pictures of the type of taxi which is a Torvane K5 in white. The taxi markings look like the pink one in the picture but to be clear his is white. The taxi is in Bermuda so if you wanted to include something island based that's ok as well but not required. The other thing he wanted to keep on there was the bermuda police crest, with the retired police office incorporated somehow.

Requirements
Must have
• Bermuda Taxi Operator
Retired Police Officer
Police Crest
Taxi #
Email
Mobile Number

```html
<!DOCTYPE html>
<html lang="en">
<head>
<meta charset="utf-8">
<title>Bermuda Taxi Operator – Business Card</title>
<link href="https://fonts.googleapis.com/css2?family=Roboto:wght@400;500;700&display=swap" rel="stylesheet">
<style>
  :root {
    --backdrop: #4a4a4a;
    --card: #ffffff;
    --brand-blue: #1f5f96;
    --text-blue: #2d5f9a;
    --rule: #9db3cf;
    --van-light: #f4f4f4;
    --van-mid: #c9c9c9;
  }
  * { box-sizing: border-box; margin: 0; padding: 0; }
  html, body {
    width: 1200px; height: 876px; overflow: hidden;
    background: var(--backdrop);
    font-family: "Roboto", Arial, sans-serif;
  }
  .canvas {
    position: relative; width: 1200px; height: 876px;
    display: flex; flex-direction: column; align-items: center; justify-content: center; gap: 56px;
  }
  .card {
    position: relative; width: 560px; height: 320px;
    background: var(--card); overflow: hidden;
  }
  /* Front */
  .crest {
    position: absolute; left: 40px; top: 56px; width: 180px;
    display: flex; flex-direction: column; align-items: center; gap: 12px;
  }
  .crest-mark {
    width: 96px; height: 96px; border-radius: 50%;
    background: var(--brand-blue);
  }
  .crest-name {
    color: var(--brand-blue); font-weight: 500; font-size: 15px; text-align: center;
  }
  .divider {
    position: absolute; left: 242px; top: 36px; width: 1.5px; height: 190px;
    background: var(--rule);
  }
  .details {
    position: absolute; left: 268px; top: 48px; color: var(--text-blue);
  }
  .details .name { font-weight: 700; font-size: 25px; color: var(--brand-blue); line-height: 1.1; }
  .details .role { font-size: 19px; margin-top: 4px; }
  .details .taxi-no { font-size: 18px; margin-top: 4px; }
  .contact { list-style: none; margin-top: 16px; font-size: 17px; }
  .contact li { display: flex; align-items: center; gap: 10px; line-height: 1.5; }
  .contact svg { width: 14px; height: 14px; flex: none; }
  .band {
    position: absolute; left: 0; right: 0; bottom: 0; height: 60px;
    background: linear-gradient(90deg, var(--brand-blue), #2c6ea8);
    display: flex; align-items: center; padding-left: 34px;
    color: #fff; font-size: 18px; font-weight: 500; letter-spacing: 0.5px; text-transform: uppercase;
  }
  /* Back */
  .crest-small {
    position: absolute; left: 238px; top: 18px;
    display: flex; align-items: center; gap: 8px;
  }
  .crest-small .crest-mark { width: 28px; height: 28px; }
  .crest-small .crest-name { font-size: 12px; }
  .vehicle {
    position: absolute; left: 70px; top: 70px; width: 440px; height: 225px;
    border-radius: 40px 90px 24px 24px;
    background: radial-gradient(ellipse at 40% 40%, var(--van-light), var(--van-mid));
  }
</style>
</head>
<body>
<main class="canvas">
  <section class="card card-front">
    <div class="crest">
      <div class="crest-mark"></div>
      <div class="crest-name">Coral Isle Police</div>
    </div>
    <div class="divider"></div>
    <div class="details">
      <p class="name">Dorian Kessler</p>
      <p class="role">Retired Police Officer</p>
      <p class="taxi-no">Taxi #T2481</p>
      <ul class="contact">
        <li>
          <svg viewBox="0 0 24 24" aria-hidden="true"><path fill="#2d5f9a" d="M6.6 10.8a15.1 15.1 0 0 0 6.6 6.6l2.2-2.2c.3-.3.7-.4 1-.2 1.1.4 2.3.6 3.6.6.6 0 1 .4 1 1V20c0 .6-.4 1-1 1A17 17 0 0 1 3 4c0-.6.4-1 1-1h3.5c.6 0 1 .4 1 1 0 1.3.2 2.5.6 3.6.1.3 0 .7-.2 1z"/></svg>
          1-441-555-0142
        </li>
        <li>
          <svg viewBox="0 0 24 24" aria-hidden="true"><rect x="2.5" y="5" width="19" height="14" rx="1.5" fill="none" stroke="#2d5f9a" stroke-width="2"/><path d="M3 6l9 7 9-7" fill="none" stroke="#2d5f9a" stroke-width="2"/></svg>
          dkessler@mailbox.com
        </li>
      </ul>
    </div>
    <div class="band">Bermuda Taxi Operator</div>
  </section>

  <section class="card card-back">
    <div class="crest-small">
      <div class="crest-mark"></div>
      <div class="crest-name">Coral Isle Police</div>
    </div>
    <div class="vehicle" role="img" aria-label="White Torvane K5 passenger van, three-quarter front view"></div>
  </section>
</main>
</body>
</html>
```